Organic, Vegan friendly and luxurious face moisturiser branding needed

Hi team

We are in the process of launching an all organic, no nasties facial moisturiser that will suite both men and woman.
We have narrowed down the bottle packaging and box packaging but need to clarify the dimensions, however we are happy to start with a few concepts. We need artwork for both the bottle and box to be designed.

The bottle will be a gloss white finish with a white dispensing pump on top. We would like to keep the colour scheme as clean as possible as the final design will be printed directly onto the bottle.
We would like to keep all text and artwork black however we are happy to explore a few shades of darker grey in the design as well.

Overall the message we want to convey through the art is one of Luxury, Pinnacle brand, eco friendliness and Organic.

Attached is a few images of artwork we like, the bottle shape will be near identical.

The brand name will be : Brumel, which means Honest in Norwegian.
We would like the tagline "Uncomplicated Skincare" to be shown somewhere on the bottle.

Ideally the front design will show the name : Brumel - Organics
Tagline "uncomplicated skincare"
Facial Moisturiser
Some sort of picture depicting the ingredients, we like floral/botanical inspiration such as some of the images attached - Ideally we want some of our ingredients to shine one the front - Some of them include:

1. Organic Aloe
2. Organic Shea
3. Green tea
4. Organic Jojoba

At the bottom front of the bottle we you will also need to display the content size, which will be 100ml/ 3.3 FL OZ

At the back the list of ingredients needs to be shown.

Aloe Barbadensis Leaf Juice (Organic Aloe), Aqua (Water), Helianthus Annuus Seed Oil (Organic Sunflower), Isopropyl Palmitate, Glyceryl Stearate SE, Cetyl Alcohol, Stearic Acid, Glycerin ( Kosher Vegetable), Butyrospermum Parkii Butter (Organic Shea), Simmondsia Chinesis Seed Oil (Organic Jojoba), Panthenol (Vitamin B5), Tocopherol Acetate (Vitamin E), Camelia Sinensis Leaf Extract (Green Tea), Xanthane Gum, Phenoxyethanol, Ethylhexylglycerin..

Alongside this we want to list the following:

1. The product is Vegan friendly
2. No Animal Testing
3 .Kosher Certified
4. Sustainable Raw Materials
5. Powered with 100% Renewable Wind Energy
6. Certified organic

You can design little logos instead of writing it out.
Updates

Hi Everyone. Please use the following template for the information on the back of the bottle. Brumel How to use: Apply twice a day to face and throat all over, or where needed. For best results, thoroughly wash face prior to use. Ingredients: Aloe Barbadensis Leaf Juice (Organic Aloe), Aqua (Water), Helianthus Annuus Seed Oil (Organic Sunflower), Isopropyl Palmitate (Plant based), Glyceryl Stearate SE (Plant based), Cetyl Alcohol (Plant based), Stearic Acid (Plant based), Glycerin ( Kosher Vegetable), Butyrospermum Parkii Butter (Organic Shea), Simmondsia Chinesis Seed Oil (Organic Jojoba), Panthenol (Vitamin B5), Tocopherol Acetate (Vitamin E), Camelia Sinensis Leaf Extract (Green Tea),  Xanthan Gum (Plant based), Phenoxyethanol (Natural preservative), Ethylhexylglycerin (Plant based) Caution: For External use only. Avoid contact with eyes. If contact occurs, rinse thoroughly with water. Keep out of reach of children. This delightful lotion absorbs right into the skin without leaving a greasy feeling yet provides the glide of a deep penetrating moisturizer. It conditions your skin while it moisturizes and softens and will leave your skin glowing. Brumel Organics info@brumelcosmetics.com Made in the USA

Industry/Entity Type

Cosmetics

Font styles to use
Serif
Sans Serif

Colors
5c5c5c
333333
000000
ffffff

Requirements
Must have
• Attached is the example of the clean bottle.
• Here are the dimensions of the bottle :
• Single Specs:
• White/White/White
• Weight: 39.67g
• Width: 47.48mm
• Height: 124.90mm
• Airless Bottle, White Cap, White Pump and Collar, White Body, 100mL

```html
<!DOCTYPE html>
<html lang="en">
<head>
<meta charset="utf-8">
<title>Brumel Facial Moisturiser – Bottle Label Artwork</title>
<link rel="stylesheet" href="https://fonts.googleapis.com/css2?family=Bodoni+Moda:wght@500;600&family=Oswald:wght@300;400;600&family=Jost:wght@400;500&display=swap">
<style>
  :root {
    --ink: #000000;
    --ink-dark: #333333;
    --ink-mid: #5c5c5c;
    --paper: #ffffff;
    --backdrop: #eef0ec;
    --panel-edge: #dcdfdb;
  }
  * { box-sizing: border-box; margin: 0; padding: 0; }
  html, body {
    width: 1200px; height: 1200px; overflow: hidden;
    background: var(--backdrop);
  }
  .artboard {
    position: relative; width: 1200px; height: 1200px;
  }
  .label {
    position: absolute; top: 290px;
    width: 380px; height: 620px;
    background: var(--paper);
    border: 1px solid var(--panel-edge);
    border-radius: 18px;
    color: var(--ink);
  }
  .label--back { left: 170px; }
  .label--front { left: 650px; }

  /* Back label */
  .back-content {
    position: absolute; left: 56px; top: 150px; width: 270px;
    font-family: "Jost", sans-serif; font-size: 8.4px; line-height: 1.6;
    color: var(--ink-dark);
  }
  .back-heading {
    font-family: "Bodoni Moda", serif; font-weight: 600; font-size: 11px;
    color: var(--ink); text-decoration: underline; text-underline-offset: 2px;
    margin-bottom: 6px;
  }
  .ingredients { margin-bottom: 26px; }
  .claims { list-style: none; margin-bottom: 72px; }
  .claims li::before { content: "• "; }
  .net-content { margin-bottom: 12px; }
  .net-content .back-heading { display: inline; margin: 0; }

  /* Front label */
  .brand-name {
    position: absolute; left: 64px; top: 120px;
    font-family: "Bodoni Moda", serif; font-weight: 600; font-size: 46px;
    line-height: 1; color: var(--ink);
  }
  .tagline {
    position: absolute; left: 64px; top: 186px;
    font-family: "Oswald", sans-serif; font-weight: 400; font-size: 16px;
    line-height: 1.2; letter-spacing: 0.5px; color: var(--ink-dark);
  }
  .tagline span {
    display: block; width: fit-content;
    border-bottom: 1.5px solid var(--ink-dark);
  }
  .botanical-art {
    position: absolute; left: 56px; top: 230px; width: 250px; height: 210px;
    background: radial-gradient(ellipse at 55% 60%, #cfcfcf 0%, #ececec 55%, var(--paper) 80%);
  }
  .product-name {
    position: absolute; left: 0; right: 0; top: 468px; text-align: center;
    font-family: "Oswald", sans-serif; font-size: 24px; color: var(--ink-dark);
  }
  .product-name strong { font-weight: 600; color: var(--ink); }
  .product-name .light { font-weight: 300; }
  .product-rule {
    position: absolute; left: 150px; top: 516px; width: 80px;
    border-top: 1px solid var(--ink-mid);
  }
  .volume {
    position: absolute; left: 0; right: 0; top: 538px; text-align: center;
    font-family: "Oswald", sans-serif; font-weight: 600; font-size: 10px;
    letter-spacing: 0.6px; color: var(--ink-dark); word-spacing: 6px;
  }
</style>
</head>
<body>
<main class="artboard">

  <section class="label label--back" aria-label="Back label">
    <div class="back-content">
      <h2 class="back-heading">ingredients :</h2>
      <p class="ingredients">Leaf Juice (Organic Aloe), Aqua (Water), Helianthus Annuus Seed Oil (Organic Sunflower), Isopropyl Palmitate, Glyceryl Stearate SE, Cetyl Alcohol, Stearic Acid, Glycerin ( Kosher Vegetable), Butyrospermum Parkii Butter (Organic Shea), Simmondsia Chinesis Seed Oil (Organic Jojoba), Panthenol (Vitamin B5), Tocopherol Acetate (Vitamin E), Camelia Sinensis Leaf Extract (Green Tea), Xanthane Gum, Phenoxyethanol, Ethylhexylglycerin..</p>

      <h2 class="back-heading">Brumel Facial Moisturiser :</h2>
      <ul class="claims">
        <li>The product is Vegan friendly</li>
        <li>No Animal Testing</li>
        <li>Kosher Certified</li>
        <li>Certified organic</li>
        <li>Sustainable Raw Materials</li>
        <li>Powered with 100% Renewable Wind Energy</li>
      </ul>

      <p class="net-content"><span class="back-heading">Net Content :</span> 100ml | 3.3 FL OZ</p>

      <h2 class="back-heading">For Feedback :</h2>
      <p class="contact">Brumel | No. 12, Linden Road | Harbor City 10021<br>Ph : +1-555-0142</p>
    </div>
  </section>

  <section class="label label--front" aria-label="Front label">
    <h1 class="brand-name">Brumel</h1>
    <p class="tagline"><span>uncomplicated</span><span>skincare</span></p>
    <div class="botanical-art" role="img" aria-label="Ink drawing of aloe and botanical leaves in black and grey"></div>
    <p class="product-name"><strong>Facial</strong> <span class="light">Moisturiser</span></p>
    <div class="product-rule"></div>
    <p class="volume">100ml 3.3 fl OZ</p>
  </section>

</main>
</body>
</html>
```